Residential building / Apartments for sale landing page

I need a website / landing page design for my latest development project - a residential building with 70+ apartments for sale. I need the design in layers in Photoshop/Illustrator/InDesign format with all the icons/shapes/maps/graphic assets in vector format (svg, ai, eps) as much as possible.

I prefer white website and please consider the performance/coding experience. We're not making something suitable only for a design contest with fancy parallax effects and confusing animations. We're trying to create usable and clean UI with good UX.

The website will be custom coded, i.e. I'm not using WordPress.

I know that the existing 3D photos are not good but for now you can use them or replace them with some stock photos. I'm going to create new 3D photos soon.

Industry/Entity Type

Real Estate Development

Number of Pages Required

1 page

```html
<!DOCTYPE html>
<html lang="en">
<head>
<meta charset="utf-8">
<title>Pine Ridge — Residential Apartments</title>
<link rel="stylesheet" href="https://fonts.googleapis.com/css2?family=Playfair+Display:wght@400&family=Open+Sans:wght@400;600;700&display=swap">
<style>
:root{
  --green:#8cbf3f;
  --ink:#2b2b2b;
  --text:#555;
  --muted:#8a8a8a;
  --light:#f4f4f6;
  --dark:#3b3b3b;
  --white:#fff;
  --serif:"Playfair Display", Georgia, serif;
  --sans:"Open Sans", Arial, sans-serif;
}
*{margin:0;padding:0;box-sizing:border-box}
html,body{width:1200px;height:4301px;overflow:hidden}
body{position:relative;background:var(--white);font-family:var(--sans);color:var(--ink)}
.abs{position:absolute}
.serif{font-family:var(--serif);font-weight:400}
.btn-outline{position:absolute;border:1.5px solid var(--ink);font-size:11px;font-weight:600;display:flex;align-items:center;justify-content:center;color:var(--ink)}
.photo{position:absolute}

/* header */
.brand{position:absolute;left:125px;top:22px;display:flex;align-items:center;gap:8px;font-weight:700;font-size:19px;color:var(--ink);letter-spacing:.5px}
.brand-mark{width:14px;height:14px;background:var(--green)}
.nav{position:absolute;left:494px;top:32px;display:flex;gap:25px;font-size:11px;color:#444}
.lang{position:absolute;left:1008px;top:33px;font-size:9px;font-weight:700}
.lang-select{position:absolute;left:1038px;top:28px;width:47px;height:25px;border:1.5px solid var(--ink);font-size:9px;display:flex;align-items:center;padding-left:10px;gap:8px}

/* hero */
.hero-panel{position:absolute;left:806px;top:75px;width:394px;height:529px;background:var(--green);color:var(--white)}
.hero-title{position:absolute;left:52px;top:82px;font-size:38px;line-height:42px;white-space:nowrap}
.hero-price{position:absolute;left:54px;top:316px;font-size:15px}
.hero-btn{position:absolute;left:64px;top:367px;width:113px;height:35px;border:1.5px solid var(--white);font-size:11px;font-weight:700;display:flex;align-items:center;justify-content:center;gap:8px}

/* stats */
.intro{left:242px;top:681px;font-size:37px;line-height:48px;white-space:nowrap}
.stat-num{font-size:56px;text-align:center;width:200px;left:770px}
.stat-label{font-family:var(--serif);font-size:13px;color:var(--muted);text-align:center;width:200px;left:770px}

/* vertical captions */
.vline{position:absolute;width:2px;background:var(--ink)}
.vtext{position:absolute;font-size:12px;white-space:nowrap;color:var(--ink)}

/* about */
.about-bg{left:502px;top:961px;width:698px;height:741px;background:var(--light)}
.section-title{font-size:46px;line-height:49px;white-space:nowrap}
.about-copy{left:609px;top:1258px;font-size:10.5px;line-height:18.7px;color:var(--muted);white-space:nowrap}

/* projects */
.tile{position:absolute;width:267px;height:180px}

/* cta band */
.cta{left:0;top:2265px;width:1200px;height:417px}
.cta-btn{position:absolute;left:828px;top:2480px;width:125px;height:34px;background:var(--green);color:var(--white);font-size:13px;display:flex;align-items:center;justify-content:center}

/* listings */
.arrow-box{position:absolute;width:47px;height:47px;background:var(--white);display:flex;align-items:center;justify-content:center}
.listing-card{position:absolute;left:394px;top:3288px;width:406px;height:153px;background:var(--white);border:2px solid #7a7a7a}
.listing-name{position:absolute;left:30px;top:22px;font-size:21px;line-height:22px}
.listing-price{position:absolute;left:254px;top:20px;font-size:26px;color:#555;font-family:var(--sans)}
.listing-price small{font-size:10px;color:var(--muted)}
.listing-desc{position:absolute;left:30px;top:82px;font-size:10px;line-height:14px;color:var(--muted);white-space:nowrap}

/* testimonial */
.quote-mark{left:0;width:1200px;text-align:center;top:3540px;font-size:40px;color:var(--ink)}
.quote{left:0;top:3597px;width:1192px;text-align:center;font-size:15.5px;line-height:23.7px;color:#8a8a8a;white-space:nowrap}
.quote-by{left:0;width:1190px;text-align:center;top:3762px;font-size:10.5px;color:var(--muted)}
.quote-by b{color:var(--ink);font-weight:600}
.dots{position:absolute;left:572px;top:3792px;display:flex;gap:4px}
.dots span{width:7px;height:7px;border-radius:50%;background:#ddd}
.dots span.on{background:var(--green)}

/* footer */
.footer{left:0;top:3852px;width:1200px;height:371px}
.footer-title{left:242px;top:3910px;font-size:35px;line-height:42px;color:var(--white)}
.contact-label{position:absolute;font-size:9px;font-weight:700;color:var(--white)}
.contact-value{position:absolute;font-size:12px;color:#c8c8c8}
.footer-links{position:absolute;font-size:11px;line-height:20px;color:#9a9a9a;list-style:none}
.footer-brand{position:absolute;left:524px;top:4096px;width:140px;display:flex;align-items:center;justify-content:center;gap:7px;font-weight:700;font-size:18px;color:#d8d8d8}
.footer-brand .brand-mark{background:#d8d8d8;width:12px;height:12px}
.news-label{position:absolute;left:733px;top:4076px;font-size:10px;color:#e0e0e0}
.news-input{position:absolute;left:731px;top:4107px;width:220px;height:32px;background:#1f1f1f;border:1px solid #555;font-size:9px;color:#ddd;display:flex;align-items:center;justify-content:space-between;padding:0 12px}
.news-btn{position:absolute;left:731px;top:4154px;width:220px;height:29px;background:var(--green);color:var(--white);font-size:9px;font-weight:700;display:flex;align-items:center;justify-content:center;gap:8px}
.copyright{left:244px;top:4256px;font-size:10px;color:#666}
.socials{position:absolute;left:888px;top:4260px;display:flex;gap:8px}
.socials span{width:7px;height:7px;border-radius:50%;background:#444}
</style>
</head>
<body>

<!-- Header -->
<div class="brand"><span class="brand-mark"></span>PINE RIDGE</div>
<nav class="nav">
  <span>Pine Ridge</span><span>The Project</span><span>Apartments/Sales</span><span>Location</span><span>Gallery</span><span>Contact Us</span>
</nav>
<div class="lang">Lang</div>
<div class="lang-select">BG
  <svg width="8" height="6" viewBox="0 0 8 6"><path d="M1 1l3 3 3-3" fill="none" stroke="#2b2b2b" stroke-width="1.4"/></svg>
</div>

<!-- Hero -->
<div class="photo" style="left:0;top:75px;width:806px;height:529px;background:linear-gradient(180deg,#dfe6ec 0%,#8fa07d 22%,#55713f 45%,#e9ece6 65%,#8f9a7f 85%,#3d3f42 100%)" role="img" aria-label="Rendering of a green terraced residential building with a mountain behind"></div>
<div class="hero-panel">
  <h1 class="hero-title serif">Sale of<br>apartments<br>directly from the<br>investor with<br>10% discount</h1>
  <p class="hero-price">Price from XXX EUR/m2</p>
  <div class="hero-btn">Buy Now
    <svg width="26" height="10" viewBox="0 0 26 10"><path d="M0 5h24M20 1l4 4-4 4" fill="none" stroke="#fff" stroke-width="1.4"/></svg>
  </div>
</div>

<!-- Intro stats -->
<h2 class="abs serif intro">We develop<br>quality infrastructure<br>and residential apartments<br>projects since 1983</h2>
<div class="abs serif stat-num" style="top:655px">70+</div>
<div class="abs stat-label" style="top:727px">Residential Apartments</div>
<div class="abs" style="left:773px;top:769px;width:192px;height:2px;background:#555"></div>
<div class="abs serif stat-num" style="top:776px">25+</div>
<div class="abs stat-label" style="top:848px">Years of Experience</div>

<!-- About -->
<div class="abs about-bg"></div>
<div class="photo" style="left:0;top:1008px;width:539px;height:648px;background:linear-gradient(180deg,#a9c6e2 0%,#c9ced3 20%,#8c8a86 55%,#6c6a64 80%,#4f5a46 100%)" role="img" aria-label="Rendering of a tall modern apartment tower with balconies"></div>
<h2 class="abs serif section-title" style="left:609px;top:1133px">Discover Our<br>Apartments.</h2>
<p class="abs about-copy">Lorem Ipsum is simply dummy text of the<br>printing and typesetting industry. Lorem Ipsum<br>has been the industry's standard dummy text<br>ever since the 1500s, when an unknown printer<br>took a galley of type and scrambled it to make<br>a type specimen book. It has survived not only<br>five centuries, but also the leap into electronic<br>typesetting, remaining essentially unchanged. It<br>was popularised in the 1960s with the release of<br>Printwell sheets containing.</p>
<div class="btn-outline" style="left:609px;top:1469px;width:104px;height:33px">Contact Us</div>
<div class="vline" style="left:949px;top:961px;height:140px"></div>
<div class="vtext" style="left:900px;top:1160px;transform:rotate(90deg)">About Pine Ridge</div>

<!-- Featured projects -->
<div class="vline" style="left:246px;top:1656px;height:180px"></div>
<div class="vtext" style="left:208px;top:1883px;transform:rotate(-90deg)">Our Projects.</div>
<h2 class="abs serif section-title" style="left:324px;top:1797px">Featured Projects.</h2>
<div class="btn-outline" style="left:324px;top:1868px;width:120px;height:33px">View all Projects</div>

<!-- CTA band -->
<div class="abs cta" style="background:linear-gradient(180deg,#3c3c3c 0%,#3c3c3c 45%,#4a4640 75%,#3a3835 100%)" role="img" aria-label="Dark city skyline at dusk"></div>

<div class="tile" style="left:324px;top:1971px;background:linear-gradient(135deg,#f1f1f1,#d8d8d8 55%,#7a5236 80%,#3a2a20)" role="img" aria-label="White kitchen with brass tap and leather stools"></div>
<div class="tile" style="left:611px;top:1971px;background:linear-gradient(180deg,#eef0f2,#cfd3d6 50%,#9b9085 85%,#7e6e5e)" role="img" aria-label="Bright open living and dining room"></div>
<div class="tile" style="left:324px;top:2175px;background:linear-gradient(90deg,#e6e2dc,#c9bfb2 40%,#8f7a69 70%,#e8e6e2)" role="img" aria-label="Bedroom with wardrobe corridor"></div>
<div class="tile" style="left:611px;top:2175px;background:linear-gradient(135deg,#e9e9e9,#d0d0d0 50%,#7a5236 78%,#3a2a20)" role="img" aria-label="Kitchen island with brass tap"></div>

<h2 class="abs serif section-title" style="left:239px;top:2443px;color:#fff">It’s time to get the<br>house of your dreams</h2>
<p class="abs" style="left:242px;top:2552px;font-size:11px;color:#bbb">For any query call us at +01 555 0148 220</p>
<div class="cta-btn">Contact Us</div>

<!-- Listings -->
<div class="vline" style="left:947px;top:2682px;height:139px"></div>
<div class="vtext" style="left:899px;top:2880px;transform:rotate(90deg)">Apartments/Sales</div>
<h2 class="abs serif section-title" style="left:242px;top:2835px;font-size:40px">Hand Picked<br>Apartments/Sales.</h2>
<div class="abs" style="left:713px;top:2897px;width:182px;height:39px;background:var(--dark);color:#fff;font-size:10.5px;font-weight:600;display:flex;align-items:center;justify-content:center">View all Apartments/Sales</div>

<div class="photo" style="left:0;top:3018px;width:340px;height:313px;background:linear-gradient(135deg,#5a5a5a,#efece6 35%,#f6f4f0 60%,#c7b08a 85%,#9a8466)" role="img" aria-label="Living room with round white table and pouf"></div>
<div class="photo" style="left:352px;top:3018px;width:481px;height:312px;background:linear-gradient(180deg,#6e9cc6 0%,#b8cfe2 30%,#e9ecec 55%,#7f8a76 80%,#5a6a46 100%)" role="img" aria-label="Rendering of a modern low-rise apartment building"></div>
<div class="photo" style="left:845px;top:3018px;width:355px;height:313px;background:linear-gradient(135deg,#b4a47a,#d8cfb6 40%,#efece4 60%,#9a6a3c 85%,#7a4e2a)" role="img" aria-label="Bedroom with upholstered bed and wooden floor"></div>
<div class="arrow-box" style="left:364px;top:3151px"><svg width="14" height="10" viewBox="0 0 14 10"><path d="M13 5H1M5 1L1 5l4 4" fill="none" stroke="#333" stroke-width="1.3"/></svg></div>
<div class="arrow-box" style="left:771px;top:3151px"><svg width="14" height="10" viewBox="0 0 14 10"><path d="M1 5h12M9 1l4 4-4 4" fill="none" stroke="#333" stroke-width="1.3"/></svg></div>

<div class="listing-card">
  <h3 class="listing-name serif">Minimal Duplex<br>Apartment</h3>
  <div class="listing-price">$347/ <small>Month</small></div>
  <p class="listing-desc">Nam in viverra mauris. Integer varius ullamcorper metus auctor porta.<br>Pellentesque velit eros, malesuada sed lorem non, rhoncus blandit leo.<br>Suspendisse lacus risus, sagittis vel laoreet at.</p>
</div>

<!-- Testimonial -->
<div class="abs serif quote-mark">66</div>
<p class="abs serif quote">Anim pariatur cliche reprehenderit, enim eiusmod high life accusamus<br>marlo finch ad squid. 3 wolf moon officia aute, non cupidatat<br>skateboard dolor brunch. Food truck quinoa nesciunt laborum eiusmod.<br>Brunch 3 wolf moon tempor, sunt aliqua put a bird on it squid<br>single-origin coffee nulla assumenda shoreditch et. Lorem Ipsum is<br>simply dummy text of the printing and typesetting industry.</p>
<p class="abs quote-by"><b>Martin Hale</b> Director of Northwind Studio</p>
<div class="dots"><span></span><span></span><span class="on"></span></div>

<!-- Footer -->
<div class="abs" style="left:0;top:3847px;width:427px;height:5px;background:var(--green)"></div>
<div class="abs footer" style="background:linear-gradient(90deg,#3a3a3a 0%,#333 50%,#2c2c2c 100%)" role="img" aria-label="Dark city towers backdrop"></div>
<h2 class="abs serif footer-title">Get<br>in touch</h2>
<div class="abs" style="left:447px;top:3906px;width:1px;height:100px;background:#777"></div>

<svg class="abs" style="left:487px;top:3931px" width="50" height="42" viewBox="0 0 50 42">
  <rect x="2" y="10" width="44" height="30" fill="none" stroke="#bbb" stroke-width="1.5"/>
  <path d="M2 10l22 17 22-17" fill="none" stroke="#bbb" stroke-width="1.5"/>
  <path d="M12 10V2h26v8" fill="none" stroke="#bbb" stroke-width="1.5"/>
</svg>
<div class="contact-label" style="left:552px;top:3946px">MAIL US :</div>
<div class="contact-value" style="left:552px;top:3962px">hello@pineridgehomes.com</div>

<svg class="abs" style="left:736px;top:3932px" width="36" height="42" viewBox="0 0 36 42">
  <path d="M9 2l7 9-4 5c2 5 6 10 11 13l5-4 7 7-5 7C16 36 3 22 2 8z" fill="none" stroke="#bbb" stroke-width="1.5"/>
</svg>
<div class="contact-label" style="left:784px;top:3946px">CALL US :</div>
<div class="contact-value" style="left:784px;top:3962px">+01 555 0148 220</div>

<ul class="footer-links" style="left:244px;top:4066px"><li>Home</li><li>Pine Ridge</li><li>The Project</li><li>Apartments/Sales</li></ul>
<ul class="footer-links" style="left:366px;top:4066px"><li>Location</li><li>Gallery</li><li>Contact Us</li></ul>

<div class="footer-brand"><span class="brand-mark"></span>PINE RIDGE</div>

<div class="news-label">Get latest news &amp; update</div>
<div class="news-input">Your Email
  <svg width="10" height="8" viewBox="0 0 10 8"><rect x=".5" y=".5" width="9" height="7" fill="none" stroke="#aaa"/><path d="M.5 .5l4.5 4 4.5-4" fill="none" stroke="#aaa"/></svg>
</div>
<div class="news-btn">SUBSCRIBE
  <svg width="20" height="8" viewBox="0 0 20 8"><path d="M0 4h18M15 1l3 3-3 3" fill="none" stroke="#fff" stroke-width="1.2"/></svg>
</div>

<div class="abs" style="left:788px;top:4226px;width:412px;height:6px;background:var(--green)"></div>
<p class="abs copyright">© 2021 PineRidge, All Rights Reserved</p>
<div class="socials"><span></span><span></span><span></span><span></span></div>

</body>
</html>
```